Bright Crest Lifts

im looking for someone to help me with my letterhead design. i have already got my logo design just need help with this part

Industry/Entity Type

Construction

Colors
0255a3

Requirements
Must have
• must have all my details eg. bank details, abn and acn

```html
<!DOCTYPE html>
<html lang="en">
<head>
<meta charset="UTF-8">
<title>Bright Crest Lifts Letterhead</title>
<link href="https://fonts.googleapis.com/css2?family=Roboto+Slab:wght@400;700&display=swap" rel="stylesheet">
<style>
  :root {
    --brand-blue: #1573ba;
    --ink: #1c1c1c;
    --muted: #444444;
    --rule: #555555;
    --paper: #ffffff;
    --watermark: #ececec;
    --band-rule: #3d3d3d;
  }
  * { margin: 0; padding: 0; box-sizing: border-box; }
  html, body { width: 950px; height: 1200px; overflow: hidden; background: var(--paper); }
  body { font-family: "Roboto Slab", Georgia, serif; color: var(--muted); }
  .letterhead { position: relative; width: 950px; height: 1200px; background: var(--paper); }

  .brand { position: absolute; left: 26px; top: 52px; display: flex; align-items: center; gap: 12px; }
  .brand-square { width: 22px; height: 22px; background: var(--brand-blue); }
  .brand-name { font-weight: 700; font-size: 30px; color: var(--ink); }

  .address { position: absolute; right: 305px; top: 40px; text-align: right; font-size: 15px; line-height: 26px; }
  .address-line { display: flex; align-items: center; justify-content: flex-end; gap: 10px; }
  .header-divider { position: absolute; left: 668px; top: 36px; width: 1px; height: 50px; background: var(--rule); }
  .contact { position: absolute; left: 686px; top: 34px; font-size: 15px; line-height: 32px; }
  .contact-line { display: flex; align-items: center; gap: 10px; }
  .email-accent { color: var(--brand-blue); }
  .icon { width: 20px; height: 20px; flex: none; }

  .watermark { position: absolute; left: 0; right: 0; top: 545px; text-align: center;
    font-weight: 700; font-size: 74px; color: var(--watermark); }

  .footer-rule { position: absolute; left: 0; right: 0; top: 1096px; height: 4px; background: var(--band-rule); }
  .footer-band { position: absolute; left: 0; right: 0; top: 1106px; bottom: 0; background: var(--brand-blue); }
  .footer-name { position: absolute; left: 590px; top: 1120px; width: 150px; text-align: center;
    font-weight: 700; font-size: 16px; color: var(--paper); }
  .footer-row { position: absolute; top: 1166px; left: 0; right: 0; height: 22px; font-size: 15px; color: var(--paper); }
  .website { position: absolute; left: 10px; display: flex; align-items: center; gap: 10px; }
  .reg-abn { position: absolute; left: 490px; }
  .reg-divider { position: absolute; left: 652px; top: -2px; width: 1px; height: 22px; background: rgba(255,255,255,0.6); }
  .reg-acn { position: absolute; left: 692px; }
</style>
</head>
<body>
<main class="letterhead">
  <header>
    <div class="brand">
      <span class="brand-square"></span>
      <span class="brand-name">Bright Crest Lifts</span>
    </div>

    <div class="address">
      <div class="address-line">
        <svg class="icon" viewBox="0 0 20 20" aria-hidden="true">
          <path d="M10 2 L1 10 H4 V18 H8 V13 H12 V18 H16 V10 H19 Z" fill="var(--brand-blue)"/>
        </svg>
        <span>Street Name, City Name</span>
      </div>
      <div>State Zipcode</div>
    </div>

    <div class="header-divider"></div>

    <div class="contact">
      <div class="contact-line">
        <svg class="icon" viewBox="0 0 20 20" aria-hidden="true">
          <circle cx="10" cy="10" r="8.5" fill="none" stroke="var(--brand-blue)" stroke-width="1.5"/>
          <path d="M7.5 5 L9 7.8 L8 9 C8.6 10.5 9.5 11.5 11 12 L12.2 11 L15 12.5 L14 14.5 C10 14.5 5.5 10 5.5 6 Z" fill="var(--brand-blue)"/>
        </svg>
        <span>123-456-7890</span>
      </div>
      <div class="contact-line">
        <svg class="icon" viewBox="0 0 20 20" aria-hidden="true">
          <rect x="2" y="5" width="16" height="11" fill="var(--brand-blue)"/>
          <path d="M2 5 L10 11 L18 5" fill="none" stroke="#fff" stroke-width="1.4"/>
        </svg>
        <span>brightcrest<span class="email-accent">lifts</span>@mail.com</span>
      </div>
    </div>
  </header>

  <div class="watermark" aria-hidden="true">Bright Crest Lifts</div>

  <footer>
    <div class="footer-rule"></div>
    <div class="footer-band"></div>

    <div class="footer-name">Bright Crest Lifts</div>

    <div class="footer-row">
      <div class="website">
        <svg class="icon" viewBox="0 0 20 20" aria-hidden="true">
          <g fill="none" stroke="#fff" stroke-width="1.2">
            <circle cx="10" cy="10" r="8"/>
            <ellipse cx="10" cy="10" rx="3.5" ry="8"/>
            <path d="M2 10 H18 M3.5 6 H16.5 M3.5 14 H16.5"/>
          </g>
        </svg>
        <span>www.brightcrestlifts.com</span>
      </div>
      <span class="reg-abn">ABN 12 456 578 655</span>
      <span class="reg-divider"></span>
      <span class="reg-acn">ACN 12 456 578 655</span>
    </div>
  </footer>
</main>
</body>
</html>
```